Sales brochure to promote delivery services

we need new revamped marketing brochure
We are a 3rd Party Logistics company specializing in home delivery and assembly for the home furnishings market. our company provides delivery services, we provide trained delivery teams, we also provide online order tracking, we provide routing and dispatching, expert handling of merchandise, white glove service. the brochure is going to be used for sales dept to leave/mail to potential customers. brochure is intended to give information about our services and attract business.

Target Market(s)

home furniture retailers, furniture and appliance retailers, retailers that require delivery services

Industry/Entity Type

Delivery Service

Requirements
Must have
• color scheme coordinates with company logo
• phone number 415.273-6150 and website address www.bravecrest-3pl.com
Nice to have
• tri-fold design preferred
• include artwork and/or pictures related to our services examples would be dining room, living room, bedroom furniture, kitchen appliances, laundry, white box delivery truck, happy customers

```html
<!DOCTYPE html>
<html lang="en">
<head>
<meta charset="utf-8">
<title>Bravecrest3PL – Home Delivery and Assembly Solutions</title>
<link rel="stylesheet" href="https://fonts.googleapis.com/css2?family=Montserrat:wght@200;300;700;800&family=Source+Sans+3:wght@400;600;700&family=Varela+Round&display=swap">
<style>
:root{
  --purple:#3b2f78;
  --yellow:#cdc711;
  --ink:#1f1f26;
  --grey:#8d8d8d;
  --night:#11131e;
  --paper:#ffffff;
  --backdrop:#4b4a4b;
}
*{margin:0;padding:0;box-sizing:border-box}
html,body{width:1200px;height:961px;overflow:hidden;background:var(--backdrop)}
.brochure{position:absolute;left:60px;top:54px;width:1076px;height:834px;overflow:hidden;background:var(--night);font-family:"Source Sans 3",sans-serif;color:var(--ink)}
.brochure svg.shapes{position:absolute;inset:0}
.abs{position:absolute}
.body-text{font-size:16.5px;line-height:21.5px}
.heading-sm{font-size:20px;line-height:24px}
.dot{fill:var(--purple)}
.bullet-dot{position:absolute;width:7px;height:7px;border-radius:50%;background:var(--purple);box-shadow:-2px 2px 0 var(--yellow)}
.helper{font-family:"Varela Round",sans-serif;color:var(--purple);font-weight:700}
.helper span{display:block;line-height:1}
.slogan{font-family:"Varela Round",sans-serif;font-weight:700;line-height:1}
.brand-name{font-family:"Montserrat",sans-serif;font-weight:800;color:var(--purple);letter-spacing:.18em;white-space:nowrap}
.company{color:#fff;text-align:center;font-size:15px;line-height:20px}
.company strong{display:block;font-size:21px;line-height:26px;font-weight:600}
.title{font-family:"Montserrat",sans-serif;line-height:1;white-space:nowrap}
.title-light{font-weight:200;color:var(--yellow)}
.title-bold{font-weight:800;color:var(--yellow);letter-spacing:-.01em}
.title-white{font-weight:800;color:#fff}
.contact{color:#fff;text-align:center}
</style>
</head>
<body>
<article class="brochure">
  <svg class="shapes" viewBox="0 0 1076 834" width="1076" height="834">
    <defs>
      <linearGradient id="roadPhoto" x1="1" y1="0" x2="0.3" y2="1">
        <stop offset="0" stop-color="#4f86c9"/>
        <stop offset="0.3" stop-color="#8fb0d4"/>
        <stop offset="0.45" stop-color="#5b6f8e"/>
        <stop offset="0.62" stop-color="#27304a"/>
        <stop offset="0.8" stop-color="#11131e"/>
      </linearGradient>
      <linearGradient id="groundShade" x1="0" y1="0" x2="0" y2="1">
        <stop offset="0.55" stop-color="#11131e" stop-opacity="0"/>
        <stop offset="0.82" stop-color="#11131e" stop-opacity="0.95"/>
        <stop offset="1" stop-color="#11131e"/>
      </linearGradient>
    </defs>
    <rect class="photo-area" x="0" y="0" width="1076" height="834" fill="url(#roadPhoto)" role="img" aria-label="Photo of a white box delivery truck driving on a highway under a blue sky"/>
    <rect x="0" y="0" width="1076" height="834" fill="url(#groundShade)"/>
    <!-- upper white panel area -->
    <path d="M0,0 L806,0 C960,40 1070,100 1040,160 L0,600 Z" fill="var(--paper)"/>
    <path d="M0,600 L1040,160 C1070,100 960,40 806,0" fill="none" stroke="var(--purple)" stroke-width="10"/>
    <!-- lower white area -->
    <path d="M0,608 L364,454 C470,490 625,540 628,574 C620,598 585,610 560,618 L0,834 Z" fill="var(--paper)"/>
    <path d="M364,454 C470,490 625,540 628,574 C620,598 585,610 560,618" fill="none" stroke="var(--yellow)" stroke-width="8"/>
    <path d="M560,618 L0,834" fill="none" stroke="var(--yellow)" stroke-width="1.5"/>
    <!-- fold lines -->
    <line x1="348" y1="0" x2="348" y2="834" stroke="#9a9a9a" stroke-opacity=".45" stroke-width="1.5"/>
    <line x1="713" y1="0" x2="713" y2="834" stroke="#9a9a9a" stroke-opacity=".45" stroke-width="1.5"/>
    <!-- leader lines -->
    <line x1="0" y1="93" x2="50" y2="93" stroke="var(--purple)" stroke-width="1.5"/>
    <circle class="dot" cx="50" cy="93" r="4"/>
    <line x1="0" y1="201" x2="50" y2="201" stroke="var(--purple)" stroke-width="1.5"/>
    <circle class="dot" cx="50" cy="201" r="4"/>
    <path d="M50,316 L50,520 C50,545 40,550 0,570" fill="none" stroke="var(--purple)" stroke-width="1.5"/>
    <circle class="dot" cx="50" cy="316" r="4"/>
    <path d="M393,0 L393,248 C393,260 400,264 412,264 L444,264" fill="none" stroke="var(--purple)" stroke-width="1.5"/>
    <circle class="dot" cx="444" cy="264" r="4"/>
  </svg>

  <!-- left panel -->
  <p class="abs body-text" style="left:70px;top:87px;width:270px">Our team of improvement prof-<br>fessionals will help you with the<br>areas that mean the most to your<br>business</p>
  <p class="abs body-text" style="left:70px;top:194px">Higher on-time delivery<br>Lower Exchanges &amp; Damaged<br>Greater Customer Satisfaction</p>
  <h3 class="abs heading-sm" style="left:70px;top:304px;font-weight:400">At Bravecrest We:</h3>
  <p class="abs body-text" style="left:70px;top:331px">Practive a simple no-nonsense<br>approach to problem solving<br>Are efficient, resourceful and<br>thorough</p>

  <div class="abs helper" style="left:88px;top:606px">
    <span style="font-size:21px">We’re Here <small style="font-size:17px">to</small></span>
    <span style="font-size:30px;margin-left:31px">Help You</span>
    <span style="font-size:19px;margin-top:-2px">Improve your</span>
    <span style="font-size:29px;margin-left:14px;margin-top:-4px">Buttom Line</span>
  </div>

  <!-- middle panel -->
  <span class="bullet-dot" style="left:418px;top:79px"></span>
  <p class="abs body-text" style="left:430px;top:70px">Bravecrest is what happens<br>when you get moving...</p>
  <span class="bullet-dot" style="left:418px;top:143px"></span>
  <p class="abs body-text" style="left:430px;top:134px">Building Bravecrest is following<br>one success immediately with<br>another.</p>

  <div class="abs slogan" style="left:464px;top:254px;font-size:24px;color:var(--grey)">When</div>
  <div class="abs slogan" style="left:451px;top:271px;font-size:24px;color:var(--ink)">You <span style="font-size:37px;color:var(--purple)">Win,</span></div>
  <div class="abs slogan" style="left:480px;top:308px;font-size:39px;color:var(--yellow)">We <span style="font-size:24px;color:var(--ink)">Win!</span></div>

  <div class="abs brand-name" style="left:419px;top:571px;font-size:11px">BRAVECREST3PL</div>

  <div class="abs company" style="left:376px;top:704px;width:320px">
    <strong>BRAVECREST3PL, INC.</strong>
    18 Harbor Point Drive Suite 400<br>
    Fremont CA 94538<br>
    Tel: 415.273-6150<br>
    Web: www.bravecrest-3pl.com
  </div>

  <!-- right / cover panel -->
  <div class="abs brand-name" style="left:777px;top:115px;font-size:17px">BRAVECREST3PL</div>

  <div class="abs title title-light" style="left:768px;top:487px;font-size:48px">HOME</div>
  <div class="abs title title-bold" style="left:792px;top:521px;font-size:45px">DELIVERY</div>
  <div class="abs title title-white" style="left:784px;top:549px;font-size:60px">AND</div>
  <div class="abs title title-bold" style="left:786px;top:603px;font-size:34px">ASSEMBLY</div>
  <div class="abs title title-light" style="left:848px;top:631px;font-size:30px">SOLUTIONS</div>

  <div class="abs contact" style="left:733px;top:758px;width:330px">
    <div style="font-size:22px;font-weight:700;line-height:28px">Tel : 415.273-6150</div>
    <div style="font-size:17.5px;line-height:26px">www.bravecrest-3pl.com</div>
  </div>
</article>
</body>
</html>
```